Vo Lunec - Business Cards & Stationnery
Think Ahead, Vo Lunec
Professional
Odile Fenwar Quintanel
48 rue des Glycines Doréales
75020 Paris
France
odile@volunec.com
www.volunec.com
The business cards have to be at the european standard ie 8,5 x 5,4 cm (seems to be 3.35'' x 2.13'')
Same for the stationnery ie A4 format, 21 x 29,7 cm (seems to be 8,27'' x 11.7'')
Please use the logo, name of the company and the base line: Think Ahead, Vo Lunec

```html
<!DOCTYPE html>
<html lang="en">
<head>
<meta charset="utf-8">
<title>Vo Lunec – Stationery</title>
<link href="https://fonts.googleapis.com/css2?family=Open+Sans:wght@400;600;700&display=swap" rel="stylesheet">
<style>
:root{
  --purple:#5b2a86;
  --purple-dark:#43196a;
  --purple-light:#8a62ad;
  --paper:#ffffff;
  --ground:#ece7df;
  --ink:#555;
  --line:#ddd;
}
*{margin:0;padding:0;box-sizing:border-box}
html,body{width:1200px;height:389px;overflow:hidden}
body{background:var(--ground);font-family:"Open Sans",sans-serif;color:var(--ink);position:relative}
.sheet{position:absolute;background:var(--paper);box-shadow:0 1px 3px rgba(0,0,0,.25);overflow:hidden}
.brand{color:var(--purple);font-weight:700;letter-spacing:.04em;display:flex;align-items:center;gap:4px;white-space:nowrap}
.brand .mark{background:var(--purple);display:inline-block}
.tag{color:var(--purple-light);font-size:4px;letter-spacing:.03em;white-space:nowrap}
.details div{white-space:nowrap}

/* business cards */
.card{width:96px;height:53px;left:29px}
.card--front{top:144px}
.card--back{top:216px}
.card--front .brand{position:absolute;left:7px;top:20px;font-size:5.5px;gap:3px}
.card--front .brand .mark{width:5px;height:5px}
.card--front .details{position:absolute;left:48px;top:14px;width:44px;font-size:2.6px;line-height:1.55;overflow:hidden}
.card--back .brand{position:absolute;left:50%;top:17px;transform:translateX(-50%);font-size:8px}
.card--back .brand .mark{width:7px;height:7px}
.card--back .tag{position:absolute;top:30px;width:100%;text-align:center}

/* letterhead */
.letter{left:139px;top:19px;width:197px;height:336px}
.letter .brand{position:absolute;left:14px;top:18px;font-size:10px}
.letter .brand .mark{width:9px;height:9px}
.letter .tag{position:absolute;left:14px;top:33px}
.letter .details{position:absolute;left:130px;top:18px;font-size:3.4px;line-height:1.5}
.letter .pattern{position:absolute;right:0;bottom:0;width:120px;height:120px;background:radial-gradient(circle at 100% 100%,rgba(91,42,134,.12),rgba(91,42,134,0) 70%)}

/* envelopes */
.envelope{left:432px;width:293px;height:101px}
.envelope--back{top:86px}
.envelope--front{top:192px}
.envelope--back svg{position:absolute;inset:0}
.envelope--back .brand{position:absolute;left:50%;top:18px;transform:translateX(-50%);font-size:8px}
.envelope--back .brand .mark{width:7px;height:7px}
.envelope--front .brand{position:absolute;left:16px;top:14px;font-size:8px}
.envelope--front .brand .mark{width:7px;height:7px}
.envelope--front .tag{position:absolute;left:16px;top:26px}
.envelope--front .pattern{position:absolute;right:0;bottom:0;width:110px;height:70px;background:radial-gradient(circle at 100% 100%,rgba(91,42,134,.1),rgba(91,42,134,0) 70%)}

/* presentation slides */
.slide{width:144px;height:99px}
.slide--1{left:739px;top:79px}
.slide--2{left:893px;top:79px}
.slide--3{left:1046px;top:79px}
.slide--4{left:739px;top:209px}
.slide--5{left:893px;top:209px}
.slide--6{left:1046px;top:209px}
.slide svg{position:absolute;inset:0}
.slide h2{position:absolute;font-size:6px;font-weight:600;color:var(--purple);white-space:nowrap}
.slide p{position:absolute;font-size:4px;line-height:1.5}
.slide--1 .brand{position:absolute;left:10px;top:12px;font-size:7px}
.slide--1 .brand .mark{width:6px;height:6px}
.slide--1 h2{right:10px;top:50px;color:#fff;font-size:7px;transform:rotate(-30deg);transform-origin:right}
.slide--2 h2{left:10px;top:10px}
.slide--3 h2{left:10px;top:10px}
.slide--3 p{left:78px;top:28px;width:58px;color:#fff}
.slide--4 .brand{position:absolute;left:10px;top:40px;font-size:7px}
.slide--4 .brand .mark{width:6px;height:6px}
.slide--4 h2{left:62px;top:14px}
.slide--4 p{left:62px;top:26px;width:72px}
.slide--5 h2{left:10px;top:10px}
.slide--6 h2{left:10px;top:10px}
</style>
</head>
<body>

<div class="sheet card card--front">
  <div class="brand"><span class="mark"></span>VO LUNEC</div>
  <div class="details">
    <div><b>Odile Fenwar Quintanel</b></div>
    <div>48 rue des Glycines Doréales</div>
    <div>75020 Paris, France</div>
    <div>odile@volunec.com</div>
    <div>www.volunec.com</div>
  </div>
</div>

<div class="sheet card card--back">
  <div class="brand"><span class="mark"></span>VO LUNEC</div>
  <div class="tag">Think Ahead, Vo Lunec</div>
</div>

<div class="sheet letter">
  <div class="brand"><span class="mark"></span>VO LUNEC</div>
  <div class="tag">Think Ahead, Vo Lunec</div>
  <div class="details">
    <div>48 rue des Glycines Doréales</div>
    <div>75020 Paris, France</div>
    <div>odile@volunec.com</div>
    <div>www.volunec.com</div>
  </div>
  <div class="pattern" role="img" aria-label="Faint square tile pattern"></div>
</div>

<div class="sheet envelope envelope--back">
  <svg width="293" height="101"><polygon points="0,0 293,0 146,44" fill="#f3f1f5" stroke="#e2dde8"/></svg>
  <div class="brand"><span class="mark"></span>VO LUNEC</div>
</div>

<div class="sheet envelope envelope--front">
  <div class="brand"><span class="mark"></span>VO LUNEC</div>
  <div class="tag">Think Ahead, Vo Lunec</div>
  <div class="pattern" role="img" aria-label="Faint square tile pattern"></div>
</div>

<div class="sheet slide slide--1">
  <svg width="144" height="99"><polygon points="60,99 144,40 144,80 95,99" fill="var(--purple)"/><polygon points="144,30 144,40 60,99 45,99" fill="var(--purple-light)"/></svg>
  <div class="brand"><span class="mark"></span>VO LUNEC</div>
  <h2>Think ahead today</h2>
</div>

<div class="sheet slide slide--2">
  <h2>Our approach</h2>
  <svg width="144" height="99">
    <g fill="var(--purple)">
      <polygon points="10,42 38,42 45,52 38,62 10,62 17,52"/>
      <polygon points="42,42 70,42 77,52 70,62 42,62 49,52"/>
      <polygon points="74,42 102,42 109,52 102,62 74,62 81,52"/>
      <polygon points="106,42 127,42 134,52 127,62 106,62 113,52"/>
    </g>
    <rect x="10" y="72" width="124" height="2" fill="var(--line)"/>
  </svg>
</div>

<div class="sheet slide slide--3">
  <svg width="144" height="99"><rect x="72" y="0" width="72" height="99" fill="var(--purple)"/><rect x="10" y="28" width="54" height="2" fill="var(--line)"/><rect x="10" y="34" width="48" height="2" fill="var(--line)"/><rect x="10" y="40" width="52" height="2" fill="var(--line)"/></svg>
  <h2>Our vision</h2>
  <p>We shape clear ideas for bold teams.</p>
</div>

<div class="sheet slide slide--4">
  <svg width="144" height="99"><rect x="0" y="84" width="144" height="15" fill="var(--purple)"/></svg>
  <div class="brand"><span class="mark"></span>VO LUNEC</div>
  <h2>Company profile</h2>
  <p>Strategy, design and growth for every client.</p>
</div>

<div class="sheet slide slide--5">
  <h2>Key figures</h2>
  <svg width="144" height="99">
    <line x1="14" y1="88" x2="134" y2="88" stroke="#bbb" stroke-width=".8"/>
    <g fill="var(--purple)">
      <rect x="20" y="46" width="10" height="42"/>
      <rect x="36" y="56" width="10" height="32"/>
      <rect x="52" y="40" width="10" height="48"/>
      <rect x="68" y="62" width="10" height="26"/>
      <rect x="84" y="50" width="10" height="38"/>
      <rect x="100" y="66" width="10" height="22"/>
      <rect x="116" y="58" width="10" height="30"/>
    </g>
  </svg>
</div>

<div class="sheet slide slide--6">
  <svg width="144" height="99"><polygon points="0,30 144,22 144,99 0,99" fill="var(--purple)"/><rect x="14" y="50" width="80" height="2" fill="var(--purple-light)"/><rect x="14" y="58" width="64" height="2" fill="var(--purple-light)"/></svg>
  <h2>Contact us today</h2>
</div>

</body>
</html>
```